Decorative concrete business needs new business cards

Our company attracts homeowners and business with disposable cash. We are a artistic decorative coatings company that will transform your driveway, patio, floors or counter tops into a work of art. We also engrave logos and designs right into the concrete! We are upscale and very professional company. I am open for rearranging our logo on the business card and also to different color patterns. We like the blue and black as in BrushNest's logo. We also like blue and orange/yellow.

Target Market(s)

Adults 30-70

Industry/Entity Type

Concrete

Contact Information for Business Card

Simple: Name, phone, email, website and social media icons

Font styles to use
Serif

Colors

Designer to choose colors to be used in the design.

Requirements
Must have
• Must present a professional upscale appearance. I have attached before and after photos that show you what our industry does. Maybe I will have before and after photo on back of card.
Nice to have
• Artistic, but bold. Nothing whimsical or cute.
Should not have
• Should not have cartoon or childlike appearance.

```html
<!DOCTYPE html>
<html lang="en">
<head>
<meta charset="utf-8">
<title>Stonecraft Surface Finishes – Business Card</title>
<link href="https://fonts.googleapis.com/css2?family=Cinzel:wght@600&family=Montserrat:wght@400;500&display=swap" rel="stylesheet">
<style>
  :root{
    --page:#3b3b3b;
    --card-dark:#050607;
    --card-light:#ffffff;
    --brand-blue:#2489c4;
    --brand-orange:#ea9420;
    --text-grey:#7a7a7a;
    --stone-light:#d9c6a3;
    --stone-mid:#b89a6c;
    --stone-dark:#8a7a66;
  }
  *{margin:0;padding:0;box-sizing:border-box}
  html,body{width:1200px;height:864px;overflow:hidden}
  body{background:var(--page);position:relative;font-family:"Montserrat",sans-serif}
  .card{position:absolute;left:354px;width:492px;border-radius:13px;overflow:hidden}
  .card-front{top:146px;height:280px;background:var(--card-dark)}
  .card-back{top:438px;height:282px;background:var(--card-light)}

  .brand-name{font-family:"Cinzel",serif;font-weight:600;color:var(--brand-blue);line-height:1.05;letter-spacing:.04em}
  .card-front .brand-lockup{position:absolute;left:0;right:0;top:108px;display:flex;justify-content:center;align-items:center;gap:12px}
  .card-front .brand-mark{width:22px;height:22px;border-radius:50%;background:var(--brand-orange)}
  .card-front .brand-name{font-size:27px;text-align:left}

  .social{position:absolute;top:233px;left:0;right:0;display:flex;justify-content:center;gap:7px}
  .social span{width:18px;height:18px;border-radius:50%;background:var(--brand-blue)}

  .card-back .brand-lockup{position:absolute;left:26px;top:36px;display:flex;align-items:center;gap:10px}
  .card-back .brand-mark{width:16px;height:16px;border-radius:50%;background:var(--brand-orange)}
  .card-back .brand-name{font-size:20px}

  .person{position:absolute;left:26px;top:136px}
  .person-name{font-size:19px;font-weight:500;color:var(--brand-blue)}
  .person-role{font-size:13.5px;color:var(--text-grey);margin-top:1px}

  .contact{position:absolute;left:26px;top:192px;list-style:none}
  .contact li{display:flex;align-items:center;gap:6px;font-size:13.5px;color:var(--text-grey);height:17px}
  .contact svg{width:12px;height:12px;flex:none}

  .project-photo{position:absolute;right:0;top:0;width:254px;height:100%;
    background:linear-gradient(180deg,#9fb4c8 0%,var(--stone-dark) 20%,var(--stone-dark) 50%,var(--stone-mid) 62%,var(--stone-light) 100%)}
  .project-photo::after{content:"";position:absolute;inset:0;
    background:linear-gradient(90deg,var(--card-light) 0%,rgba(255,255,255,.6) 12%,rgba(255,255,255,0) 32%)}
</style>
</head>
<body>
  <section class="card card-front">
    <div class="brand-lockup">
      <span class="brand-mark"></span>
      <div class="brand-name">Stonecraft<br>Surface<br>Finishes</div>
    </div>
    <div class="social" aria-label="Social media">
      <span></span><span></span><span></span>
    </div>
  </section>

  <section class="card card-back">
    <div class="project-photo" role="img" aria-label="Photo of a finished stamped concrete driveway in front of a garage"></div>
    <div class="brand-lockup">
      <span class="brand-mark"></span>
      <div class="brand-name">Stonecraft<br>Surface Finishes</div>
    </div>
    <div class="person">
      <div class="person-name">Daniel Reyes</div>
      <div class="person-role">President</div>
    </div>
    <ul class="contact">
      <li><svg viewBox="0 0 12 12"><path d="M2 10c0-5 3-8 8-8l1 2-2 1c-2 0-4 2-4 4l1 2-2 1z" fill="#ea9420"/></svg>555-014-2876</li>
      <li><svg viewBox="0 0 12 12"><rect x="3" y="0.5" width="6" height="11" rx="1.2" fill="none" stroke="#ea9420" stroke-width="1.2"/><circle cx="6" cy="9.5" r=".7" fill="#ea9420"/></svg>555-014-2877</li>
      <li><svg viewBox="0 0 12 12"><rect x="0.5" y="2.5" width="11" height="7" fill="#ea9420"/><path d="M.5 2.5 6 6.5l5.5-4" fill="none" stroke="#fff" stroke-width="1"/></svg>hello@stonecraftfinish.com</li>
      <li><svg viewBox="0 0 12 12" fill="none" stroke="#ea9420" stroke-width="1"><circle cx="6" cy="6" r="5.2"/><ellipse cx="6" cy="6" rx="2.3" ry="5.2"/><path d="M1 6h10M2 3.3h8M2 8.7h8"/></svg>www.stonecraftfinish.com</li>
    </ul>
  </section>
</body>
</html>
```